magcian / mentalist needs flyer desined to send potentisl clients

I need a design that's contemporary, sharp, fun, and professional that will get the attention of whoever receives the flyer very quickly. This is for a tri-fold flyer design.

I've been performing magic for over 40 years. I've performed close-up,
parlor, and stage shows. I've been an Master of Ceremonies, Key Note
Speaker (using magic during presentations to help build on a point or
topic, while keeping the audience entertained and educated on the topic or
topics the client has asked me to focus). I've worked trade shows and
sales training incorporating magic as well. I did private shows in Las
Vegas and L.A. back in the late 90's as well.

I do have website / tobiaskellwoodillusions.example for your to check out.

Target Market(s)

The target audience is corporation Event Planners, Marketing and Sales
managers, casino & hotel entertainment directors, as well as private
businesses looking for unique entertainment options.

Industry/Entity Type

Entertainment Industry

Logo Text

Here are a couple of ideas: your mind is my playground, neural entertainer, professor of mysteries, master of your mind

Requirements
Must have
• I like the black and white look (I think it looks nice, but open to other
• ideas and creativity. Being I'm a magician and mentalist, I'd like for
• both venues to be conveyed somehow. My magic is clean and corporate and family friendly.
Nice to have
• I do have website / tobiaskellwoodillusions.example for your to check out.
• My current business card is attached for review. I'll also attach photos
• I'd like to share, but was unable when I last attempted do sign up. Some
• of the files were too big and I'm not savvy enough to make them smaller,
• but think there might be some potential with a couple.
Should not have
• cartoons or cartoonish graphics. no rabbits, doves, magicians, wands, or top hats.

```html
<!DOCTYPE html>
<html lang="en">
<head>
<meta charset="utf-8">
<title>Tobias Kellwood Illusions – Tri-fold Flyer</title>
<link href="https://fonts.googleapis.com/css2?family=Montserrat:wght@600&family=Open+Sans:wght@400;600;700&display=swap" rel="stylesheet">
<style>
  :root {
    --backdrop: #e4e3e1;
    --ink: #0b0b0b;
    --brand-blue: #1f7bc6;
    --brand-blue-deep: #1a6db2;
    --pill-blue: #2a82cf;
    --paper: #ffffff;
  }
  html, body {
    margin: 0;
    width: 1200px;
    height: 900px;
    overflow: hidden;
    background: var(--backdrop);
    font-family: "Open Sans", Arial, sans-serif;
  }
  .canvas { position: relative; width: 1200px; height: 900px; }
  .artwork { position: absolute; left: 0; top: 0; }
  .flyer-shadow { filter: drop-shadow(2px 3px 3px rgba(0,0,0,.35)); }

  .pill {
    position: absolute;
    background: var(--pill-blue);
    color: var(--paper);
    border-radius: 5px;
    box-sizing: border-box;
    white-space: nowrap;
    overflow: hidden;
  }
  .brand-title {
    left: 756px; top: 148px; width: 280px; height: 33px;
    font-family: "Montserrat", Arial, sans-serif;
    font-weight: 600; font-size: 14.5px; letter-spacing: .3px;
    line-height: 30px; text-align: center;
    border: 1.5px solid #6fb3ea;
  }
  .tagline {
    position: absolute; left: 760px; top: 199px; width: 272px; margin: 0;
    color: var(--paper); font-weight: 700; font-size: 10px;
    line-height: 15px; text-align: center; text-transform: uppercase;
  }
  .cta-box {
    position: absolute; left: 473px; top: 238px; width: 264px; height: 22px;
    background: var(--paper); border-radius: 4px; color: #111;
    font-family: Arial, Helvetica, sans-serif;
    font-size: 13.5px; line-height: 22px; text-align: center; white-space: nowrap;
  }
  .contact-line {
    position: absolute; left: 450px; width: 298px;
    color: var(--paper); font-weight: 700; font-size: 10.5px; text-align: center;
  }
  .section-pill {
    left: 177px; top: 493px; width: 161px; height: 21px;
    font-weight: 700; font-size: 12px; line-height: 21px; padding-left: 7px;
  }
  .body-copy {
    position: absolute; left: 176px; width: 247px;
    color: var(--paper); font-size: 9.3px; line-height: 11.6px;
    letter-spacing: -.1px; text-align: justify; margin: 0;
  }
  .subhead {
    position: absolute; left: 176px; top: 599px;
    color: var(--paper); font-weight: 700; font-size: 11px; margin: 0;
  }
  .web-pill {
    left: 790px; top: 715px; width: 192px; height: 22px;
    font-weight: 700; font-size: 10.5px; line-height: 22px; text-align: center;
  }
</style>
</head>
<body>
<div class="canvas">
  <svg class="artwork" width="1200" height="900" viewBox="0 0 1200 900" xmlns="http://www.w3.org/2000/svg">
    <defs>
      <linearGradient id="warmPhoto" x1="0" y1="0" x2="1" y2="1">
        <stop offset="0" stop-color="#c9a27c"/>
        <stop offset=".6" stop-color="#9a6a48"/>
        <stop offset="1" stop-color="#3a2a22"/>
      </linearGradient>
      <linearGradient id="roomPhoto" x1="0" y1="0" x2="0" y2="1">
        <stop offset="0" stop-color="#a8553c"/>
        <stop offset=".45" stop-color="#c49a74"/>
        <stop offset="1" stop-color="#2e2a28"/>
      </linearGradient>
      <radialGradient id="stagePhoto" cx=".5" cy=".5" r=".6">
        <stop offset="0" stop-color="#5a4035"/>
        <stop offset="1" stop-color="#141010"/>
      </radialGradient>
      <radialGradient id="tablePhoto" cx=".5" cy=".4" r=".6">
        <stop offset="0" stop-color="#c9ac8c"/>
        <stop offset="1" stop-color="#6b5444"/>
      </radialGradient>
      <clipPath id="flyerClip"><rect x="153" y="125" width="892" height="630"/></clipPath>
    </defs>

    <g class="flyer-shadow">
      <rect x="153" y="125" width="892" height="630" fill="var(--ink)"/>
    </g>

    <g clip-path="url(#flyerClip)">
      <rect class="panel-middle" x="450" y="125" width="298" height="630" fill="var(--brand-blue)"/>
      <g class="panel-middle-circles" fill="var(--brand-blue-deep)" opacity=".7">
        <circle cx="690" cy="190" r="75"/>
        <circle cx="560" cy="330" r="105"/>
        <circle cx="520" cy="460" r="90"/>
      </g>

      <path d="M153,125 H478 C430,195 385,255 330,290 C275,322 240,360 226,410 C210,465 185,487 153,492 Z"
            fill="none" stroke="var(--paper)" stroke-width="14"/>
      <path role="img" aria-label="Photo: magician performing close-up magic for a guest at a conference table"
            d="M153,125 H478 C430,195 385,255 330,290 C275,322 240,360 226,410 C210,465 185,487 153,492 Z"
            fill="url(#warmPhoto)"/>
      <circle cx="313" cy="382" r="76" fill="var(--paper)"/>
      <circle role="img" aria-label="Photo: magician performing for seated guests at a banquet table"
              cx="313" cy="382" r="70" fill="url(#tablePhoto)"/>

      <path d="M1045,275 C900,258 765,300 692,388 C640,450 610,520 545,618 C512,665 486,705 474,755 H1045 Z"
            fill="none" stroke="var(--paper)" stroke-width="14"/>
      <path role="img" aria-label="Photo: guest holding a string trick with the magician at a busy corporate event"
            d="M1045,275 C900,258 765,300 692,388 C640,450 610,520 545,618 C512,665 486,705 474,755 H1045 Z"
            fill="url(#roomPhoto)"/>
      <circle cx="578" cy="577" r="87" fill="var(--paper)"/>
      <circle role="img" aria-label="Photo: magician performing a rope routine on stage with an assistant"
              cx="578" cy="577" r="80" fill="url(#stagePhoto)"/>
    </g>

    <g class="contact-icons" fill="none" stroke="var(--paper)" stroke-width="1.3">
      <circle cx="599" cy="289" r="7"/>
      <path d="M596,285.5 l1.6,-.8 1.4,2.2 -1,1 c.6,1.3 1.4,2.1 2.6,2.6 l1,-1 2.2,1.4 -.8,1.6 c-4,.2 -7.2,-3 -7,-7z" fill="var(--paper)" stroke="none"/>
      <circle cx="599" cy="321" r="7"/>
      <rect x="594.5" y="317.8" width="9" height="6.4" fill="var(--paper)" stroke="none"/>
      <path d="M594.5,318 L599,321.6 L603.5,318" stroke="var(--brand-blue)" stroke-width="1"/>
      <circle cx="599" cy="353" r="7"/>
      <circle cx="599" cy="353" r="4.5" stroke-width="1"/>
      <path d="M594.5,353 H603.5 M599,348.5 V357.5 M596.8,349 C595.6,351.5 595.6,354.5 596.8,357 M601.2,349 C602.4,351.5 602.4,354.5 601.2,357" stroke-width=".8"/>
    </g>

    <g class="social-squares" fill="var(--paper)">
      <rect x="539" y="409" width="17" height="17" rx="2"/>
      <rect x="562" y="409" width="17" height="17" rx="2"/>
      <rect x="585" y="409" width="17" height="17" rx="2"/>
      <rect x="608" y="409" width="17" height="17" rx="2"/>
      <rect x="631" y="409" width="17" height="17" rx="2"/>
    </g>
  </svg>

  <div class="pill brand-title">TOBIAS KELLWOOD ILLUSIONS</div>
  <p class="tagline">Magic at your corporate function<br>adds an element that will distinguish<br>your company from others.</p>

  <div class="cta-box">Contact Tobias today to elevate your event!</div>
  <div class="contact-line" style="top:297px">505-555-0142</div>
  <div class="contact-line" style="top:329px">hello@tobiaskellwoodillusions.example</div>
  <div class="contact-line" style="top:365px">tobiaskellwoodillusions.example</div>

  <div class="pill section-pill">Why should you hire me?</div>
  <p class="body-copy" style="top:524px">I have been performing magic since age 8, and have a love and passion for making people smile and laugh, but here are some other reasons.<br>&nbsp;I’ve performed all over the country for major corporations which means you’re getting tried and true, first-rate entertainment.</p>
  <p class="subhead">My performances are guaranteed!</p>
  <p class="body-copy" style="top:620px">I pride myself on building relationships with my customers, so I’m not happy unless you’re happy. I guarantee your guests will have a great time and will thank you for having me there. If you aren’t thrilled with my performance, just let me know and I’ll refund your money. The only reason I’m able to offer such a guarantee is because I’m very confident you will love doing business with me. In four decades of performing, I’ve never had anyone ask for their money back, and many of my clients hire me again and again.</p>

  <div class="pill web-pill">tobiaskellwoodillusions.example</div>
</div>
</body>
</html>
```